Smart, intuitive SaaS software dashboard design

PactBloom is an innovative modern SaaS (software as a service) solution for contract and meeting management.

What we are looking for is fresh ideas for our dashboard. We do not need web coding or actionable wireframes now – but purely great design ideas from where to continue forward.

How should a modern web software dashboard look like? Fresh, intuitive, easy-to-use, and adaptable for responsive mobile designs. We hope that when the user logs into the service and sees the dashboard, he/she gets a good big picture of the current status of the most important documents of his/hers company.

To get to know the service and see the components, we kindly ask you to register to our service at www.pactbloom-demo.net and to utilize the free trial (30 days) so you can see the existing dashboard live. And also try out how it works. Might help you to get ideas how to improve it.

(The designer we will choose might be offered later on to design some other pages as well (contract view and edit pages, meeting page etc).)

You’ll find additional information in the attachment.

You’ll find more information of the company and the service also at www.pactbloom-demo.net

Target Market(s)

Global

Industry/Entity Type

Business Management

Number of Pages Required

1 page

Font styles to use
Sans Serif

Requirements
Must have
• 1) Clear design idea for us to iterate from, 2) Modern look and feel - elegant & bold at the same time - still with credibility in our target group. And 3) Suitable for dashboard usage - it should it a clear big picture for the user.
• UPDATE:
• Users should see most important things with one glance. Therefore we would like to see AT LEAST these items mentioned below on the first page.
• NOTE: if all these things are visible on the dashboard, the menu list is maybe not needed on the left. (And there might be some icons on the top header with needed settings/inbox features anyway.)
• NOTE2: as explained earlier, the design should be responsive i.e. work without modifications in PC, iPad and mobile (the areas/boxes would just rearrange themselves on top of each other.)
• -First area should be Documents, which would include different document categories: Contracts, Finance & Admin and HR
• -All different types of Meetings could be the next area (upcoming ones clearly visible with date and maybe description, time and location visible also).
• -Reminders and Activity Feed (they might also be together in top of each other, so that Reminder is visible first and Activity feed can be chosen from the tab.)
• -Virtual Datarooms (maybe 1-3 different ones with some analytics for each visible e.g. like usage/visits per day)
• Saved searches in very important list as users can save their most important searches. There are typically many of these, so at least 5 should be visible and then see all button (maybe even more could be visible if they fit on your design)
• My Latest is also important.
• (As explained, Action Required area is NOT needed anymore).
Nice to have
• Surprise us!
Should not have
• Please avoid the boring traditional legacy stuff and the common report dashboards.
• You do not need design a 100% mockup for the techie to continue with. The ideas count.

```html
<!DOCTYPE html>
<html lang="en">
<head>
<meta charset="utf-8">
<title>PactBloom Dashboard</title>
<link href="https://fonts.googleapis.com/css2?family=Roboto:wght@400;500;700&display=swap" rel="stylesheet">
<style>
:root{
  --green:#7dcc00;
  --green-dark:#69ad00;
  --dark:#1b1b1b;
  --dark-2:#262626;
  --dark-3:#303030;
  --page:#efefef;
  --panel:#f9f9f9;
  --white:#ffffff;
  --line:#e2e2e2;
  --text:#222222;
  --muted:#8a8a8a;
  --icon:#b5b5b5;
}
*{box-sizing:border-box;margin:0;padding:0}
html,body{width:1159px;height:1200px;overflow:hidden;background:var(--page)}
body{font-family:'Roboto',Arial,sans-serif;color:var(--text)}
.stage{position:absolute;left:0;top:0;width:966px;height:1000px;transform:scale(1.2);transform-origin:0 0;background:var(--page)}
.abs{position:absolute}

/* header */
.topbar{left:0;top:0;width:966px;height:64px;background:var(--dark)}
.brand{left:22px;top:14px;display:flex;align-items:center;gap:8px;color:var(--white);font-size:19px;font-weight:500;letter-spacing:.5px}
.brand-dot{width:34px;height:34px;border-radius:50%;border:4px solid var(--green)}
.search{left:224px;top:17px;width:269px;height:30px;border-radius:15px;background:var(--white);overflow:hidden;display:flex}
.search-field{flex:1;font-size:10px;color:#9a9a9a;padding:10px 14px}
.search-scope{width:90px;background:var(--green);color:var(--white);font-size:10px;font-weight:500;display:flex;align-items:center;justify-content:center;gap:8px}
.add-btn{left:510px;top:17px;width:30px;height:30px;border-radius:50%;border:2px solid var(--green);display:flex;align-items:center;justify-content:center}
.notice{top:24px}
.badge{position:absolute;top:-4px;right:-7px;width:12px;height:12px;border-radius:50%;background:var(--green);color:var(--white);font-size:7px;font-weight:700;display:flex;align-items:center;justify-content:center}
.user{left:675px;top:0;width:160px;height:64px;background:var(--dark-3);display:flex;align-items:center;gap:12px;padding-left:20px;color:#e6e6e6;font-size:10.5px}
.avatar{width:34px;height:34px;border-radius:50%;background:radial-gradient(circle at 50% 40%,#8a8a8a,#3a3a3a);border:2px solid #555}
.help{left:835px;top:0;width:63px;height:64px;border-left:1px solid #333;border-right:1px solid #333;display:flex;align-items:center;justify-content:center;color:var(--white);font-size:11px;font-weight:700}
.logout{left:898px;top:0;width:68px;height:64px;display:flex;align-items:center;justify-content:center}
.user-menu{left:675px;top:64px;width:160px;background:var(--dark-2);z-index:5}
.user-menu li{list-style:none;height:35.5px;display:flex;align-items:center;gap:12px;padding-left:26px;color:#e0e0e0;font-size:10px;border-bottom:1px solid #333}
.user-menu li:last-child{border-bottom:0}

/* tabs & panels */
.tabs{display:flex;gap:6px}
.tab{height:35px;display:flex;align-items:center;justify-content:center;gap:7px;font-size:13px;font-weight:500;color:var(--white);background:var(--green)}
.tab.active{background:var(--panel);color:var(--text);border-top:3px solid var(--green)}
.panel{background:var(--panel);border:1px solid #e8e8e8}
.btn-dark{display:inline-flex;align-items:center;justify-content:center;gap:6px;height:24px;padding:0 14px;background:#2b2b2b;color:var(--white);font-size:9.5px;font-weight:500;border:1px solid #111}

/* documents */
.docs-tabs{left:22px;top:86px;width:652px}
.docs{left:22px;top:121px;width:652px;height:314px;border-top:0}
.doc-row{position:absolute;left:22px;width:610px;height:65px;border-bottom:1px solid var(--line);display:flex;align-items:center}
.doc-icon{width:48px;display:flex;justify-content:center;margin-left:10px}
.doc-main{border-left:1px solid var(--line);padding-left:14px;height:34px;width:312px;display:flex;flex-direction:column;justify-content:center}
.doc-title{font-size:11.5px;color:var(--text)}
.doc-meta{font-size:8.5px;color:var(--muted);margin-top:3px}
.doc-meta b{font-weight:400;color:#555}
.doc-stats{border-left:1px solid var(--line);height:34px;display:flex;align-items:center;gap:12px;padding-left:21px;font-size:9px;color:var(--muted)}
.doc-stats span{display:flex;align-items:center;gap:4px}

/* meetings */
.meetings{left:22px;top:457px;width:652px;height:464px}
.meetings-head{height:35px;background:var(--green);color:var(--white);font-size:13px;font-weight:500;display:flex;align-items:center;padding-left:22px}
.meeting{position:absolute;left:20px;width:612px;height:92px;border-bottom:1px solid var(--line)}
.date-card{position:absolute;left:1px;top:13px;width:48px;height:64px;background:var(--white);text-align:center}
.date-num{font-size:29px;line-height:46px;color:var(--text)}
.date-month{position:absolute;left:0;bottom:0;width:48px;height:16px;background:var(--green);color:var(--white);font-size:8.5px;line-height:16px}
.meeting-body{position:absolute;left:84px;top:14px;width:430px}
.meeting-title{font-size:11.5px}
.meeting-text{font-size:8.5px;color:#666;line-height:12.5px;margin-top:3px}
.meeting-meta{font-size:9px;color:var(--muted);margin-top:7px;display:flex;gap:8px;align-items:center}
.meeting-actions{position:absolute;left:541px;top:13px;height:64px;border-left:1px solid var(--line);display:flex;align-items:center;gap:12px;padding-left:27px}

/* activity */
.feed-tabs{left:697px;top:86px;width:247px}
.side-tab{height:34px;display:flex;align-items:center;justify-content:center;font-size:10.5px;color:#aaa;background:#e8e8e8}
.side-tab.active{background:var(--panel);color:var(--text);border-top:3px solid var(--green)}
.feed{left:697px;top:120px;width:247px;height:369px;border-top:0}
.timeline{position:absolute;left:24px;top:10px;width:1px;height:300px;background:var(--line)}
.event{position:absolute;left:41px;width:190px;font-size:8.5px;color:#666;line-height:12px}
.event .when{color:#aaa;font-size:9.5px;margin-bottom:4px}
.event::before{content:"";position:absolute;left:-22px;top:3px;width:7px;height:7px;border-radius:50%;background:var(--green)}
.event.current .when{color:var(--text)}
.event.current .what{color:var(--green);text-decoration:underline}
.event.cut::before{display:none}

/* saved / latest */
.saved-tabs{left:697px;top:511px;width:247px}
.saved{left:697px;top:546px;width:247px;height:375px;border-top:0}
.saved-item{position:absolute;left:0;width:247px;height:65px;display:flex;align-items:center}
.saved-item .inner{margin-left:22px;width:201px;height:65px;border-bottom:1px solid var(--line);display:flex;align-items:center;gap:11px;font-size:9.5px;color:#777;line-height:14px}
.saved-item.hl{background:var(--white);box-shadow:0 2px 6px rgba(0,0,0,.06)}
.saved-item.hl .inner{border-bottom:0;color:#555}

/* footer */
.footer{left:0;top:943px;width:966px;height:57px;background:var(--dark)}
.copy{left:22px;top:23px;font-size:9.5px;color:#9a9a9a}
.social{left:697px;top:17px;display:flex;gap:5px}
.social span{width:22px;height:22px;border-radius:50%;display:block}
.trust{left:885px;top:14px;width:52px;height:29px;border-radius:4px;background:#f0c419}
</style>
</head>
<body>
<div class="stage">

  <header class="abs topbar">
    <div class="abs brand"><span class="brand-dot"></span>PactBloom</div>
    <div class="abs search">
      <div class="search-field">Search ...</div>
      <div class="search-scope">Contracts
        <svg width="7" height="5" viewBox="0 0 7 5"><path d="M1 1l2.5 2.5L6 1" stroke="#fff" stroke-width="1.4" fill="none"/></svg>
      </div>
    </div>
    <div class="abs add-btn"><svg width="12" height="12" viewBox="0 0 12 12"><path d="M6 1v10M1 6h10" stroke="#7dcc00" stroke-width="2.4"/></svg></div>
    <div class="abs notice" style="left:578px">
      <svg width="16" height="14" viewBox="0 0 16 14" fill="#8a8a8a"><circle cx="5" cy="4" r="3"/><circle cx="11" cy="4" r="2.5"/><path d="M0 13c0-4 2-6 5-6s5 2 5 6z"/><path d="M10 7c3 0 6 1.5 6 5h-5c0-2-.3-3.6-1-5z"/></svg>
      <span class="badge">3</span>
    </div>
    <div class="abs notice" style="left:620px">
      <svg width="13" height="14" viewBox="0 0 13 14" fill="#8a8a8a"><path d="M6.5 0c3 0 4.5 2.3 4.5 5v3l2 3H0l2-3V5c0-2.7 1.5-5 4.5-5z"/><circle cx="6.5" cy="12.5" r="1.5"/></svg>
      <span class="badge">7</span>
    </div>
    <div class="abs user"><div class="avatar" role="img" aria-label="User profile photo"></div>Marco Linden</div>
    <div class="abs help">?</div>
    <div class="abs logout"><svg width="12" height="11" viewBox="0 0 12 11" fill="#ddd"><path d="M0 1h5v1.5H1.5v6H5V10H0z"/><path d="M4 4h4V1.5L12 5.5 8 9.5V7H4z"/></svg></div>
  </header>

  <ul class="abs user-menu">
    <li><svg width="8" height="9" viewBox="0 0 8 9" fill="#999"><circle cx="4" cy="2.3" r="2.3"/><path d="M0 9c0-3 1.7-4.3 4-4.3S8 6 8 9z"/></svg>My Profile</li>
    <li><svg width="9" height="7" viewBox="0 0 9 7" fill="#999"><path d="M0 0h9v7H0z"/><path d="M0 0l4.5 3.5L9 0" stroke="#222" fill="none"/></svg>Inbox</li>
    <li><svg width="9" height="9" viewBox="0 0 9 9" fill="#999"><circle cx="4.5" cy="4.5" r="3.3"/><circle cx="4.5" cy="4.5" r="1.3" fill="#222"/><path d="M4 0h1v2H4zM4 7h1v2H4zM0 4h2v1H0zM7 4h2v1H7z"/></svg>Settings</li>
  </ul>

  <!-- documents -->
  <nav class="abs tabs docs-tabs">
    <div class="tab active" style="width:115px">
      <svg width="11" height="12" viewBox="0 0 11 12" fill="none" stroke="#222" stroke-width="1.3"><rect x="3" y="1" width="7" height="8"/><path d="M1 3v8h7"/></svg>Contracts</div>
    <div class="tab" style="width:153px">$ Finance &amp; Admin</div>
    <div class="tab" style="width:372px">
      <svg width="11" height="11" viewBox="0 0 11 11" fill="none" stroke="#fff" stroke-width="1.6"><path d="M9.5 4A4.2 4.2 0 0 0 1.5 4.5M1.5 7a4.2 4.2 0 0 0 8-.5"/><path d="M9.8 1v3.2H6.6M1.2 10V6.8h3.2"/></svg>Transfer Pricing</div>
  </nav>

  <section class="abs panel docs">
    <div class="doc-row" style="top:2px">
      <div class="doc-icon"><svg width="22" height="27" viewBox="0 0 22 27" fill="none" stroke="#aaa" stroke-width="1.3"><path d="M1 1h14l6 6v19H1z"/><path d="M15 1v6h6"/><text x="11" y="20" font-size="10" font-family="Arial" fill="#aaa" stroke="none" text-anchor="middle" font-weight="700">W</text></svg></div>
      <div class="doc-main"><div class="doc-title">Agreement Trio 2015-10-11.dox</div><div class="doc-meta">Date Modified: <b>27-06-2016, 14:27,</b> &nbsp;Size: <b>437 KB</b></div></div>
      <div class="doc-stats"><span>▦ Total: 154,</span><span>⧗ Starred 42,</span><span>↻ In Progress 7</span></div>
    </div>
    <div class="doc-row" style="top:67px">
      <div class="doc-icon"><svg width="22" height="27" viewBox="0 0 22 27" fill="none" stroke="#aaa" stroke-width="1.3"><path d="M1 1h14l6 6v19H1z"/><path d="M15 1v6h6"/><path d="M6 20c3-2 6-7 5-10s-3 4 0 7 5 2 5 2"/></svg></div>
      <div class="doc-main"><div class="doc-title">Agreement Trio 2015-10-11.pdf</div><div class="doc-meta">Date Modified: <b>27-06-2016, 14:27,</b> &nbsp;Size: <b>437 KB</b></div></div>
      <div class="doc-stats"><span>▦ Total: 154,</span><span>⧗ Starred 42,</span><span>↻ In Progress 7</span></div>
    </div>
    <div class="doc-row" style="top:132px">
      <div class="doc-icon"><svg width="22" height="27" viewBox="0 0 22 27" fill="none" stroke="#aaa" stroke-width="1.3"><path d="M1 1h14l6 6v19H1z"/><path d="M15 1v6h6"/><text x="11" y="20" font-size="10" font-family="Arial" fill="#aaa" stroke="none" text-anchor="middle" font-weight="700">W</text></svg></div>
      <div class="doc-main"><div class="doc-title">Agreement Trio 2015-10-11.dox</div><div class="doc-meta">Date Modified: <b>27-06-2016, 14:27,</b> &nbsp;Size: <b>437 KB</b></div></div>
      <div class="doc-stats"><span>▦ Total: 154,</span><span>⧗ Starred 42,</span><span>↻ In Progress 7</span></div>
    </div>
    <div class="doc-row" style="top:197px">
      <div class="doc-icon"><svg width="22" height="27" viewBox="0 0 22 27" fill="none" stroke="#aaa" stroke-width="1.3"><path d="M1 1h14l6 6v19H1z"/><path d="M15 1v6h6"/><rect x="5" y="11" width="12" height="10"/><circle cx="9" cy="14.5" r="1.2" fill="#aaa"/><path d="M5 20l4-3 3 2 2-2 3 3" /></svg></div>
      <div class="doc-main"><div class="doc-title">Agreement Trio 2015-10-11.jpg</div><div class="doc-meta">Date Modified: <b>27-06-2016, 14:27,</b> &nbsp;Size: <b>437 KB</b></div></div>
      <div class="doc-stats"><span>▦ Total: 154,</span><span>⧗ Starred 42,</span><span>↻ In Progress 7</span></div>
    </div>
    <div class="btn-dark abs" style="left:22px;top:268px">Show All</div>
  </section>

  <!-- meetings -->
  <section class="abs panel meetings">
    <div class="meetings-head">Upcoming Meetings</div>
    <div class="meeting" style="top:43px">
      <div class="date-card"><div class="date-num">15</div><div class="date-month">January</div></div>
      <div class="meeting-body"><div class="meeting-title">Board Meeting</div><div class="meeting-text">It is a long established fact that a reader will be distracted by the readable content of a page when looking at its layout. The point of using Lorem Ipsum is that ...</div><div class="meeting-meta">◷ 11 A.M &nbsp;/ &nbsp;⌖ Meeting Location</div></div>
      <div class="meeting-actions"><svg width="10" height="11" viewBox="0 0 10 11" fill="none" stroke="#aaa" stroke-width="1.2"><path d="M0 2h10M3.5 2V.6h3V2M1.5 2l.7 8.4h5.6L8.5 2"/></svg><svg width="13" height="12" viewBox="0 0 13 12" fill="none" stroke="#aaa" stroke-width="1.2"><path d="M7 2H1v9h9V6"/><path d="M11 .8l1.2 1.2L6 8.2 4.5 8.5 4.8 7z"/></svg></div>
    </div>
    <div class="meeting" style="top:135px">
      <div class="date-card"><div class="date-num">16</div><div class="date-month">January</div></div>
      <div class="meeting-body"><div class="meeting-title">Board Meeting</div><div class="meeting-text">It is a long established fact that a reader will be distracted by the readable content of a page when looking at its layout. The point of using Lorem Ipsum is that ...</div><div class="meeting-meta">◷ 11 A.M &nbsp;/ &nbsp;⌖ Meeting Location</div></div>
      <div class="meeting-actions"><svg width="10" height="11" viewBox="0 0 10 11" fill="none" stroke="#aaa" stroke-width="1.2"><path d="M0 2h10M3.5 2V.6h3V2M1.5 2l.7 8.4h5.6L8.5 2"/></svg><svg width="13" height="12" viewBox="0 0 13 12" fill="none" stroke="#7dcc00" stroke-width="1.4"><path d="M7 2H1v9h9V6"/><path d="M11 .8l1.2 1.2L6 8.2 4.5 8.5 4.8 7z"/></svg></div>
    </div>
    <div class="meeting" style="top:227px">
      <div class="date-card"><div class="date-num">18</div><div class="date-month">January</div></div>
      <div class="meeting-body"><div class="meeting-title">Shareholder's Meeting</div><div class="meeting-text">It is a long established fact that a reader will be distracted by the readable content of a page when looking at its layout. The point of using Lorem Ipsum is that ...</div><div class="meeting-meta">◷ 11 A.M &nbsp;/ &nbsp;⌖ Meeting Location</div></div>
      <div class="meeting-actions"><svg width="10" height="11" viewBox="0 0 10 11" fill="none" stroke="#aaa" stroke-width="1.2"><path d="M0 2h10M3.5 2V.6h3V2M1.5 2l.7 8.4h5.6L8.5 2"/></svg><svg width="13" height="12" viewBox="0 0 13 12" fill="none" stroke="#aaa" stroke-width="1.2"><path d="M7 2H1v9h9V6"/><path d="M11 .8l1.2 1.2L6 8.2 4.5 8.5 4.8 7z"/></svg></div>
    </div>
    <div class="meeting" style="top:319px;border-bottom:0">
      <div class="date-card"><div class="date-num">23</div><div class="date-month">January</div></div>
      <div class="meeting-body"><div class="meeting-title">Board Meeting</div><div class="meeting-text">It is a long established fact that a reader will be distracted by the readable content of a page when looking at its layout. The point of using Lorem Ipsum is that ...</div><div class="meeting-meta">◷ 11 A.M &nbsp;/ &nbsp;⌖ Meeting Location</div></div>
      <div class="meeting-actions"><svg width="10" height="11" viewBox="0 0 10 11" fill="none" stroke="#aaa" stroke-width="1.2"><path d="M0 2h10M3.5 2V.6h3V2M1.5 2l.7 8.4h5.6L8.5 2"/></svg><svg width="13" height="12" viewBox="0 0 13 12" fill="none" stroke="#aaa" stroke-width="1.2"><path d="M7 2H1v9h9V6"/><path d="M11 .8l1.2 1.2L6 8.2 4.5 8.5 4.8 7z"/></svg></div>
    </div>
    <div class="btn-dark abs" style="left:20px;top:419px">Show All</div>
  </section>

  <!-- reminders / activity -->
  <nav class="abs tabs feed-tabs" style="gap:0">
    <div class="side-tab active" style="width:88px">Reminders</div>
    <div class="side-tab" style="width:98px">Activity Feed</div>
  </nav>
  <section class="abs panel feed">
    <div class="timeline"></div>
    <div class="event cut" style="top:42px"><div class="what">Vivamus finibus diam in feugiat gravida.<br>Sed dapibus</div></div>
    <div class="event" style="top:91px"><div class="when">29.62016</div><div class="what">Section 1.10.32 of "de Finibus<br>Bonorum et Malorum</div></div>
    <div class="event current" style="top:147px"><div class="when">29.62016</div><div class="what">Vivamus finibus diam in feugiat gravida.<br>Sed dapibus</div></div>
    <div class="event" style="top:203px"><div class="when">29.62016</div><div class="what">Section 1.10.32 of "de Finibus<br>Bonorum et Malorum</div></div>
    <div class="event" style="top:259px"><div class="when">29.62016</div><div class="what">Vivamus finibus diam in feugiat gravida.<br>Sed dapibus</div></div>
    <div class="btn-dark abs" style="left:19px;top:323px">
      <svg width="9" height="9" viewBox="0 0 9 9" fill="#fff"><path d="M0 1.5h9V9H0z"/><path d="M2 0h1v2H2zM6 0h1v2H6z"/><path d="M1 3.5h7v4.5H1z" fill="#2b2b2b"/></svg>Calendar</div>
  </section>

  <!-- saved searches / latest -->
  <nav class="abs tabs saved-tabs" style="gap:0">
    <div class="side-tab" style="width:119px">Saved Searches</div>
    <div class="side-tab active" style="width:90px;height:35px;margin-top:0">My Latest</div>
  </nav>
  <section class="abs panel saved">
    <div class="saved-item" style="top:0"><div class="inner"><svg width="8" height="7" viewBox="0 0 8 7"><path d="M1 3.5l2 2L7 1" stroke="#aaa" stroke-width="1.6" fill="none"/></svg>Business consultant<br>agreement Hale &amp; Hale</div></div>
    <div class="saved-item hl" style="top:64px"><div class="inner"><svg width="8" height="7" viewBox="0 0 8 7"><path d="M1 3.5l2 2L7 1" stroke="#7dcc00" stroke-width="1.8" fill="none"/></svg>Business Agreement<br>Whitford</div></div>
    <div class="saved-item" style="top:129px"><div class="inner"><svg width="8" height="7" viewBox="0 0 8 7"><path d="M1 3.5l2 2L7 1" stroke="#aaa" stroke-width="1.6" fill="none"/></svg>Confidentiality Agreement<br>Hale &amp; Hale</div></div>
    <div class="saved-item" style="top:194px"><div class="inner"><svg width="8" height="7" viewBox="0 0 8 7"><path d="M1 3.5l2 2L7 1" stroke="#aaa" stroke-width="1.6" fill="none"/></svg>Confidentiality Agreement<br>Hale &amp; Hale</div></div>
    <div class="saved-item" style="top:259px"><div class="inner" style="border-bottom:0"><svg width="8" height="7" viewBox="0 0 8 7"><path d="M1 3.5l2 2L7 1" stroke="#aaa" stroke-width="1.6" fill="none"/></svg>Confidentiality Agreement<br>Hale &amp; Hale</div></div>
    <div class="btn-dark abs" style="left:16px;top:329px">
      <svg width="9" height="9" viewBox="0 0 9 9" fill="#fff"><path d="M0 1.5h9V9H0z"/><path d="M2 0h1v2H2zM6 0h1v2H6z"/><path d="M1 3.5h7v4.5H1z" fill="#2b2b2b"/></svg>Calendar</div>
  </section>

  <footer class="abs footer">
    <div class="abs copy">© 2016 PactBloom Ltd. Terms of Use &nbsp;/ &nbsp;Privacy</div>
    <div class="abs social">
      <span style="background:#3b5998"></span>
      <span style="background:#cb2027"></span>
      <span style="background:#29a9e1"></span>
      <span style="background:#d42d24"></span>
    </div>
    <div class="abs trust"></div>
  </footer>

</div>
</body>
</html>
```